Start-up lawncare company needing marketing flyer to promote business model

Hello! We are looking for a marketing flyer design with the requirements below.

We would like the size to fit a flyer that is 6.25" X 9", Front and Back.

We need these to meet the NPDS RCMX requirements, there are details attached for the indicias that need to be included, and where to put them on the back of the flyer.

Here's the items items we would like to have included on the flyer:
- Logo (Attached)

- I attached a snip of how our website looks, as well as how our app looks, and would like to follow that general color scheme

- References to our YardMint App, in both Quorvex and Plinth stores, and our website (www.YardMint.example)

- Reference to the neighborhood barometer and gets the point across that the more of their neighbors that sign up, the cheaper the price of service (Visual attached of what this barometer looks like)

- We are licensed and insured landscaping pros

- Real, instant, upfront pricing for mowing, mulching and most other services

- Sign up with a few easy steps and manage your account from our app or online

- Automated safe & secure transactions upon service completion and satisfaction

- Excellent customer service with our quality guaranteed commitment!

- Sign up now and receive 50% off your first mow!

- Veteran owned

- A portion of our proceeds go to "Rowan Ellery Foundation"

- List's out all of the services we will offer
- Mowing
- Mulching
- Aeration and Over-seeding
- Fertilization
- Shrub/Tree Trimming
- Leaf removal and yard clean up
- Accent lighting installation
- Sprinkler blow-out / Winterization
- Driveway pressure washing and sealing
- Firewood Delivery

Target Market(s)

Homeowners in large neighborhoods that need lawn care services

Industry/Entity Type

Lawn Care

Font styles to use
Sans Serif

Colors

Designer to choose colors to be used in the design.

Requirements
Must have
• Meet NPDS RCMX requirements
• Keep a similar color scheme to our website, feel free to use bold accents to make it more eye-catching as people search through their mail
• Get the general point across that as more of their neighbors sign up with us, the cheaper their service will be

```html
<!DOCTYPE html>
<html lang="en">
<head>
<meta charset="utf-8">
<title>YardMint Flyer – Front and Back</title>
<link href="https://fonts.googleapis.com/css2?family=Montserrat:wght@400;500;700;800&display=swap" rel="stylesheet">
<style>
  :root{
    --bg:#333333;
    --green:#3cb64a;
    --green-dark:#1c7a34;
    --green-panel:#23893b;
    --navy:#1f3f9e;
    --sky:#21a7df;
    --white:#ffffff;
    --ink:#1b1b1b;
    --tick:#2d4fb3;
  }
  *{box-sizing:border-box;margin:0;padding:0}
  html,body{width:1200px;height:1200px;overflow:hidden;background:var(--bg)}
  body{position:relative;font-family:"Montserrat",sans-serif;color:var(--ink)}

  /* ---------- Front side ---------- */
  .front{position:absolute;left:54px;top:58px;width:757px;height:531px;background:var(--white);overflow:hidden}
  .front-header{position:absolute;left:0;top:0;width:100%;height:141px;
    background:linear-gradient(90deg,var(--green) 0%,#2a9d43 60%,var(--green-dark) 100%)}
  .front-header h1{position:absolute;left:29px;top:28px;color:var(--white);font-weight:800;
    font-size:29px;line-height:36px;letter-spacing:.5px}
  .pill{position:absolute;background:var(--navy);color:var(--white);font-weight:700;
    border-radius:0 18px 18px 0;display:flex;align-items:center}
  .front .pill{left:0;top:155px;width:144px;height:25px;font-size:18px;padding-left:31px}
  .features{position:absolute;left:29px;top:193px;width:440px;list-style:none}
  .features li{position:relative;padding-left:19px;font-size:14px;line-height:16px;margin-bottom:11.5px;font-weight:500}
  .features li svg,.services li svg{position:absolute;left:0;top:3px}
  .brand{position:absolute;left:378px;top:380px;display:flex;align-items:center;gap:7px}
  .brand-dot{width:16px;height:16px;border-radius:50%;background:var(--green-dark)}
  .brand-name{font-weight:800;font-size:26px;color:var(--green-dark)}
  .app-preview{position:absolute;left:530px;top:30px;width:200px;height:426px;border-radius:34px;
    background:linear-gradient(180deg,#3cb870 0%,#2ba35c 100%)}
  .front-footer{position:absolute;left:0;top:463px;width:100%;height:68px;background:var(--sky)}
  .footer-text{color:var(--white);font-weight:700;font-size:14px;line-height:17px}
  .front .footer-text{position:absolute;left:46px;top:14px}
  .store-badge{position:absolute;top:15px;width:89px;height:26px;background:#111;border-radius:4px;border:1px solid #555}
  .store-a{left:537px}.store-b{left:636px}

  /* ---------- Back side ---------- */
  .back{position:absolute;left:374px;top:614px;width:760px;height:533px;background:var(--white);overflow:hidden}
  .back-left{position:absolute;left:0;top:0;width:388px;height:100%;background:var(--green-panel)}
  .lawn-photo{position:absolute;left:0;top:0;width:388px;height:290px;
    background:linear-gradient(180deg,#4f6a3a 0%,#3f8a2e 40%,#3a9a30 75%,var(--green-panel) 100%)}
  .back .pill{left:0;top:292px;width:224px;height:31px;font-size:20px;padding-left:20px;letter-spacing:.5px}
  .services{position:absolute;top:333px;list-style:none;color:var(--white)}
  .services li{position:relative;padding-left:15px;font-size:12.5px;line-height:15px;margin-bottom:5.5px}
  .services.col-a{left:20px;width:150px}
  .services.col-b{left:171px;width:215px;top:331px}
  .back-footer{position:absolute;left:0;top:469px;width:388px;height:64px;background:var(--sky)}
  .back .footer-text{position:absolute;left:35px;top:12px}
  .back-right{position:absolute;left:388px;top:0;width:372px;height:100%}
  .savings-banner{position:absolute;left:0;top:0;width:100%;height:130px;background:var(--green);
    color:var(--white);font-weight:800;font-size:12.5px;line-height:16.5px;text-align:center;padding-top:16px}
  .savings-banner p+p{margin-top:11px}
  .barometer{position:absolute;left:62px;top:160px}
  .indicia{position:absolute;left:274px;top:322px;width:60px;height:60px;border:1px solid #555;
    font-family:Arial,sans-serif;font-size:8px;line-height:9.5px;text-align:center;padding-top:5px;color:#111}
  .address{position:absolute;left:115px;top:424px;width:187px;height:70px;border:1.5px solid #222;
    font-family:Arial,sans-serif;font-size:10.5px;color:#111;padding:6px 12px}
  .address .line-top{font-size:10px;text-align:center;margin-bottom:18px}
  .address p{line-height:13px}
</style>
</head>
<body>

<section class="front">
  <header class="front-header">
    <h1>SIGN UP NOW AND<br>RECEIVE 50% OFF YOUR<br>FIRST MOW!</h1>
  </header>

  <div class="pill">Features</div>
  <ul class="features">
    <li><svg width="11" height="9" viewBox="0 0 11 9"><rect x=".5" y="2" width="7" height="6.5" fill="none" stroke="#2d4fb3"/><path d="M2 5l2 2 6-6" fill="none" stroke="#2d4fb3" stroke-width="1.5"/></svg>We are licensed and insured landscaping pros</li>
    <li><svg width="11" height="9" viewBox="0 0 11 9"><rect x=".5" y="2" width="7" height="6.5" fill="none" stroke="#2d4fb3"/><path d="M2 5l2 2 6-6" fill="none" stroke="#2d4fb3" stroke-width="1.5"/></svg>Real, instant, upfront pricing for mowing, mulching and most other services</li>
    <li><svg width="11" height="9" viewBox="0 0 11 9"><rect x=".5" y="2" width="7" height="6.5" fill="none" stroke="#2d4fb3"/><path d="M2 5l2 2 6-6" fill="none" stroke="#2d4fb3" stroke-width="1.5"/></svg>Sign up with a few easy steps and manage your account from our app or online</li>
    <li><svg width="11" height="9" viewBox="0 0 11 9"><rect x=".5" y="2" width="7" height="6.5" fill="none" stroke="#2d4fb3"/><path d="M2 5l2 2 6-6" fill="none" stroke="#2d4fb3" stroke-width="1.5"/></svg>Automated safe &amp; secure transactions upon service completion and satisfaction</li>
    <li><svg width="11" height="9" viewBox="0 0 11 9"><rect x=".5" y="2" width="7" height="6.5" fill="none" stroke="#2d4fb3"/><path d="M2 5l2 2 6-6" fill="none" stroke="#2d4fb3" stroke-width="1.5"/></svg>Excellent customer service with our quality<br>guaranteed commitment!</li>
    <li><svg width="11" height="9" viewBox="0 0 11 9"><rect x=".5" y="2" width="7" height="6.5" fill="none" stroke="#2d4fb3"/><path d="M2 5l2 2 6-6" fill="none" stroke="#2d4fb3" stroke-width="1.5"/></svg>Veteran owned</li>
    <li><svg width="11" height="9" viewBox="0 0 11 9"><rect x=".5" y="2" width="7" height="6.5" fill="none" stroke="#2d4fb3"/><path d="M2 5l2 2 6-6" fill="none" stroke="#2d4fb3" stroke-width="1.5"/></svg>A portion of our proceeds go to "Rowan Ellery<br>Foundation"</li>
  </ul>

  <div class="brand"><span class="brand-dot"></span><span class="brand-name">YardMint</span></div>

  <div class="app-preview" role="img" aria-label="Smartphone showing the YardMint app instant quote screen with mowing, mulching and additional services options"></div>

  <footer class="front-footer">
    <p class="footer-text">For more information please visit<br>our website&nbsp; www.YardMint.example</p>
    <div class="store-badge store-a" role="img" aria-label="Quorvex store download badge"></div>
    <div class="store-badge store-b" role="img" aria-label="Plinth store download badge"></div>
  </footer>
</section>

<section class="back">
  <div class="back-left">
    <div class="lawn-photo" role="img" aria-label="Photo of a neatly mown green lawn framed by garden shrubs and plants"></div>
    <div class="pill">Services We Offer</div>
    <ul class="services col-a">
      <li><svg width="9" height="8" viewBox="0 0 9 8"><path d="M1 4l2 2 5-5" fill="none" stroke="#fff" stroke-width="1.2"/></svg>Mowing</li>
      <li><svg width="9" height="8" viewBox="0 0 9 8"><path d="M1 4l2 2 5-5" fill="none" stroke="#fff" stroke-width="1.2"/></svg>Mulching</li>
      <li><svg width="9" height="8" viewBox="0 0 9 8"><path d="M1 4l2 2 5-5" fill="none" stroke="#fff" stroke-width="1.2"/></svg>Aeration and<br>Over-seeding</li>
      <li><svg width="9" height="8" viewBox="0 0 9 8"><path d="M1 4l2 2 5-5" fill="none" stroke="#fff" stroke-width="1.2"/></svg>Fertilization</li>
      <li><svg width="9" height="8" viewBox="0 0 9 8"><path d="M1 4l2 2 5-5" fill="none" stroke="#fff" stroke-width="1.2"/></svg>Shrub/<br>Tree Trimming</li>
    </ul>
    <ul class="services col-b">
      <li><svg width="9" height="8" viewBox="0 0 9 8"><path d="M1 4l2 2 5-5" fill="none" stroke="#fff" stroke-width="1.2"/></svg>Leaf removal and yard clean up</li>
      <li><svg width="9" height="8" viewBox="0 0 9 8"><path d="M1 4l2 2 5-5" fill="none" stroke="#fff" stroke-width="1.2"/></svg>Accent lighting installation</li>
      <li><svg width="9" height="8" viewBox="0 0 9 8"><path d="M1 4l2 2 5-5" fill="none" stroke="#fff" stroke-width="1.2"/></svg>Sprinkler blow-out /<br>Winterization</li>
      <li><svg width="9" height="8" viewBox="0 0 9 8"><path d="M1 4l2 2 5-5" fill="none" stroke="#fff" stroke-width="1.2"/></svg>Driveway pressure washing<br>and sealing</li>
      <li><svg width="9" height="8" viewBox="0 0 9 8"><path d="M1 4l2 2 5-5" fill="none" stroke="#fff" stroke-width="1.2"/></svg>Firewood Delivery</li>
    </ul>
    <footer class="back-footer">
      <p class="footer-text">For more information please visit our<br>website&nbsp; www.YardMint.example</p>
    </footer>
  </div>

  <div class="back-right">
    <div class="savings-banner">
      <p>YOU COULD SAVE UPTO 10 % OFF OUR ALREADY<br>LOW PRICES, AS MORE OF YOUR<br>NEIGHBORS SIGN UP !</p>
      <p>CHECK OUT APP TODAY TO SEE HOW MUCH<br>NEIGHBOURS ARE ALREADY SAVING !</p>
    </div>

    <svg class="barometer" width="240" height="80" viewBox="0 0 240 80" role="img" aria-label="Neighborhood savings barometer from 0 to 10 percent">
      <defs>
        <linearGradient id="baro" x1="0" x2="1">
          <stop offset="0" stop-color="#c98f63"/>
          <stop offset=".45" stop-color="#a9adba"/>
          <stop offset="1" stop-color="#e8b44c"/>
        </linearGradient>
      </defs>
      <rect x="0" y="61" width="237" height="18" rx="9" fill="#e6e6e6"/>
      <rect x="0" y="61" width="193" height="18" rx="9" fill="url(#baro)"/>
      <text x="110" y="75" font-family="Montserrat,sans-serif" font-weight="700" font-size="11" fill="#fff" text-anchor="middle">5%</text>
      <text x="212" y="75" font-family="Montserrat,sans-serif" font-weight="700" font-size="11" fill="#fff" text-anchor="middle">10%</text>
      <!-- small house -->
      <g fill="#cd8a5a"><path d="M15 36l15-13 15 13z"/><rect x="19" y="36" width="22" height="14"/></g>
      <rect x="24" y="40" width="4" height="4" fill="#fff"/><rect x="31" y="40" width="4" height="4" fill="#fff"/>
      <!-- medium house -->
      <g fill="#a1a6b5"><path d="M84 30l23-20 23 20z"/><rect x="90" y="30" width="34" height="20"/></g>
      <rect x="97" y="36" width="7" height="7" fill="#fff"/><rect x="110" y="36" width="7" height="7" fill="#fff"/>
      <!-- large house -->
      <g fill="#e8b44c"><path d="M161 28l29-26 29 26z"/><rect x="168" y="28" width="44" height="24"/></g>
      <rect x="177" y="36" width="8" height="16" fill="#fff"/><rect x="193" y="36" width="10" height="9" fill="#fff"/>
    </svg>

    <div class="indicia">PRSRT STD<br>ECRWSS<br>U.S.POSTAGE<br>PAID<br>RCMX RETAIL</div>

    <div class="address">
      <p class="line-top">****************ECRWSSRCMX****</p>
      <p>Postal Customer</p>
      <p>City, State, 5-Digit ZIP Code</p>
    </div>
  </div>
</section>

</body>
</html>
```